cartNest - a stylish trolley for apartments

We neede a simple website to sell our Trolley, for apartment use.
The colour theme is red, blask & white. Our logo is attached and this needs to be on the Home page.
The website only needs a Home Page plus 4 other pges.
In the attachment you will find a site map.

You can check out the following two sites to see what I like:
www.plinthgallery.example/design-showcase-inspiration/minimalist-portfolio-website/
www.brightquarry.example/inspiration/40-beautiful-web-design-portfolios/ in this site especially
Dario Menezes
K B Forge
Nine 17 Studio
Oliver Marsh

And especially Lamp - I ike the simpicity of the site esp as we are only selling one product

Target Market(s)

Apartment dwellers

Industry/Entity Type

Apartment

Requirements
Must have
• This website must have 4 pages.
We need Corvo, Ledgerline and Quidly portals.
Order Form for Trolley
Payment form.

```html
<!DOCTYPE html>
<html lang="en">
<head>
<meta charset="utf-8">
<title>cartNest – a stylish trolley for apartments</title>
<link href="https://fonts.googleapis.com/css2?family=Bebas+Neue&family=Cutive&family=Questrial&family=Yanone+Kaffeesatz:wght@300&family=Shadows+Into+Light&display=swap" rel="stylesheet">
<style>
  :root {
    --red: #c40000;
    --red-dark: #8e0000;
    --ink: #1a1a1a;
    --grey: #7a7a7a;
    --paper: #f7f7f7;
    --canvas-edge: #c9c9c9;
  }
  * { margin: 0; padding: 0; box-sizing: border-box; }
  html, body { width: 1200px; height: 720px; overflow: hidden; }
  body {
    position: relative;
    background: radial-gradient(ellipse 520px 420px at 600px 330px, #ffffff 0%, #ececec 55%, var(--canvas-edge) 100%);
    font-family: "Questrial", sans-serif;
    color: var(--ink);
  }
  .brand-tile {
    position: absolute; left: 216px; top: 0; width: 144px; height: 146px;
    background: var(--paper);
    box-shadow: 0 6px 6px -4px rgba(0,0,0,.35);
    display: flex; align-items: flex-end; justify-content: center; gap: 6px;
    padding-bottom: 18px;
  }
  .brand-tile .brand-dot { width: 10px; height: 10px; background: var(--red); border-radius: 50%; margin-bottom: 7px; }
  .brand-tile .brand-name { font-family: "Questrial", sans-serif; font-size: 25px; color: var(--ink); }
  .main-nav {
    position: absolute; top: 25px; left: 464px; right: 0;
    font-size: 15px; font-weight: 700;
  }
  .main-nav a { position: absolute; color: var(--red); text-decoration: none; white-space: nowrap; }
  .hero-photo {
    position: absolute; left: 472px; top: 72px; width: 200px; height: 320px;
    background: radial-gradient(ellipse at 50% 55%, #8f8f8f 0%, #c8c8c8 55%, rgba(240,240,240,0) 78%);
  }
  .tagline {
    position: absolute; left: 752px; top: 158px;
    font-family: "Cutive", serif; font-size: 29px; line-height: 36px; color: var(--ink);
  }
  .tagline-shadow {
    position: absolute; left: 732px; top: 320px; width: 175px; height: 16px;
    background: radial-gradient(ellipse at center, rgba(0,0,0,.22), rgba(0,0,0,0) 70%);
  }
  .pointer-arrow { position: absolute; left: 462px; top: 380px; }
  .buy-button {
    position: absolute; left: 514px; top: 418px; width: 130px; height: 36px;
    border-radius: 7px;
    background: linear-gradient(#d41010, var(--red) 50%, var(--red-dark));
    color: #fff; text-align: center; text-decoration: none;
    font-family: "Bebas Neue", sans-serif; font-size: 20px; line-height: 38px; letter-spacing: .5px;
  }
  .pitch { position: absolute; left: 275px; top: 496px; width: 640px; }
  .pitch h1 {
    font-family: "Bebas Neue", sans-serif; font-weight: 400; font-size: 20px; line-height: 23px;
    color: var(--red); letter-spacing: .2px;
  }
  .pitch p {
    margin-top: 2px;
    font-family: "Yanone Kaffeesatz", sans-serif; font-weight: 300; font-size: 17px; line-height: 19px;
    color: var(--ink);
  }
  .copyright {
    position: absolute; left: 0; width: 1159px; top: 686px; text-align: center;
    font-family: Arial, sans-serif; font-size: 8px; color: var(--grey);
  }
  .social { position: absolute; left: 846px; top: 664px; width: 92px; text-align: center; }
  .social .label { font-family: "Shadows Into Light", cursive; font-size: 13px; color: var(--grey); }
  .social .links { font-family: "Questrial", sans-serif; font-size: 9px; color: #6a6a6a; margin-top: 3px; display: flex; justify-content: center; gap: 8px; }
</style>
</head>
<body>
  <div class="brand-tile">
    <span class="brand-dot"></span><span class="brand-name">cartNest</span>
  </div>

  <nav class="main-nav">
    <a href="#" style="left:0">cartNest</a>
    <a href="#" style="left:96px">Gallery</a>
    <a href="#" style="left:182px">Contact Us</a>
    <a href="#" style="left:300px">Shopping Cart payment</a>
  </nav>

  <div class="hero-photo" role="img" aria-label="Photo of a chrome bellhop-style trolley loaded with suitcases and hanging garments"></div>

  <div class="tagline">cartNest<br>evolved<br>from<br>demand!</div>
  <div class="tagline-shadow"></div>

  <svg class="pointer-arrow" width="36" height="64" viewBox="0 0 36 64" aria-hidden="true">
    <path d="M14 2 C2 20 2 48 30 59" fill="none" stroke="#c8c8c8" stroke-width="2"/>
    <path d="M22 52 L30 59 L20 62" fill="none" stroke="#c8c8c8" stroke-width="2"/>
  </svg>

  <a class="buy-button" href="#">Buy Now</a>

  <section class="pitch">
    <h1>Apartment dwellers everywhere are calling for a solution to moving shopping, luggage<br>and other goods from car to apartment, and vice versa</h1>
    <p>Other trolleys on the market are not versatile, they are not robust, but more importantly, they are NOT stylish!<br>
    The emphasis of cartNest is on style. This trolley is stylish enough to remain in your apartment as a piece of<br>
    furniture. It features a versatile flat-bed and hanger, to cope with all your transport needs.</p>
  </section>

  <div class="copyright">copyright 2012, cartNest, all rights reserved</div>

  <div class="social">
    <div class="label">Connect with us</div>
    <div class="links"><span>Chatterbook</span><span>Chirpline</span></div>
  </div>
</body>
</html>
```